Velmint website

A clean uncluttered design that shows at glance that we are in the Media and design and publishing business.

We would like to see designs that use colours that show warmth and quality.

The website should show:
- products
- projects

These should be displaxed in spaces that we can add or interchanges with new products or projects.
Updates

Target Market(s)

Business and project managers and buyers and authors.

Industry/Entity Type

Business

Requirements
Must have
• Good colours. Not too strong, not weak, but reflecting quality.

```html
<!DOCTYPE html>
<html lang="en">
<head>
<meta charset="utf-8">
<title>Velmint – World News &amp; Media Services</title>
<link rel="stylesheet" href="https://fonts.googleapis.com/css2?family=Open+Sans:wght@300;400;600&amp;display=swap">
<style>
:root{
  --page-bg:#ececec;
  --white:#ffffff;
  --navy:#0d3470;
  --blue:#1f5a98;
  --brand:#1d4f86;
  --gold:#d9a01a;
  --text:#333333;
  --muted:#8a8a8a;
  --line:#d6d6d6;
}
*{box-sizing:border-box;margin:0;padding:0}
html,body{width:991px;height:1200px;overflow:hidden}
body{background:var(--page-bg);font-family:'Open Sans',Arial,sans-serif;color:var(--text);position:relative}
.page{position:absolute;left:52px;top:0;width:887px;height:1103px;background:var(--white)}
.abs{position:absolute}

/* header */
.logo{left:30px;top:18px;font-size:44px;font-weight:400;color:var(--brand);letter-spacing:1px;line-height:1}
.slogan{left:32px;top:67px;font-size:14.5px;color:var(--brand)}
.search{left:643px;top:16px;width:217px;height:27px;border:1px solid var(--line);font-size:11px;font-style:italic;color:#999;padding:6px 11px}
.search svg{position:absolute;right:9px;top:6px}
.nav{right:27px;top:66px;display:flex;font-size:14.5px;color:#444}
.nav span{padding:0 12px;border-left:1px solid #bbb;line-height:18px}
.nav span:first-child{border-left:none}
.nav span:last-child{padding-right:0}

/* hero */
.hero{left:0;top:102px;width:887px;height:335px;background:linear-gradient(180deg,#2a6aa6 0%,#154b88 55%,#0a2f68 100%)}
.hero .map{left:433px;top:58px;width:425px;height:217px;border-radius:45%;background:radial-gradient(ellipse at center,rgba(255,255,255,.18) 0%,rgba(255,255,255,.05) 60%,rgba(255,255,255,0) 75%)}
.hero h1{left:55px;top:82px;font-size:32px;font-weight:400;color:var(--white);line-height:1.2}
.hero h2{left:55px;top:120px;font-size:28px;font-weight:300;color:var(--white);line-height:1.2}
.hero p{left:57px;top:160px;width:400px;font-size:11.5px;line-height:19px;color:#c9d7ea}
.dots{left:58px;top:206px;display:flex;gap:6px}
.dots i{width:11px;height:11px;border-radius:50%;background:var(--white);display:block}
.dots i.on{background:var(--gold)}

/* featured */
.section-title{font-size:21px;font-weight:400}
.featured-title{left:22px;top:455px;color:var(--gold)}
.project{top:491px;width:193px;height:184px;border:1px solid var(--line);border-radius:3px}
.project .photo{position:absolute;left:12px;top:10px;width:172px;height:96px;border-radius:3px}
.project h3{position:absolute;left:13px;top:113px;font-size:17px;font-weight:400;color:#444}
.project p{position:absolute;left:13px;top:138px;width:172px;font-size:10.5px;line-height:16px;color:var(--muted)}

.video{left:630px;top:454px;width:245px;height:211px;border:1px solid #e2e2e2;border-radius:3px}
.video .photo{position:absolute;left:0;top:0;width:243px;height:138px;background:linear-gradient(100deg,#3a3f4a 0%,#8b8f99 40%,#c7883a 75%,#e0a64a 100%)}
.video svg{position:absolute;left:103px;top:52px}
.video h3{position:absolute;left:16px;top:146px;font-size:17px;font-weight:400;color:var(--gold)}
.video p{position:absolute;left:16px;top:169px;width:215px;font-size:9.5px;line-height:15px;color:var(--muted)}

/* welcome */
.welcome h2{position:absolute;left:24px;top:704px;font-size:22.5px;font-weight:400;color:#333;white-space:nowrap}
.welcome p{position:absolute;left:25px;top:735px;width:600px;font-size:11.4px;line-height:19px;color:var(--muted)}
.divider{left:22px;top:834px;width:588px;height:1px;background:var(--line)}

/* products */
.products-title{left:26px;top:852px;color:var(--brand)}
.arrows{left:558px;top:860px}
.product{top:890px;width:178px;height:181px;border-radius:3px;box-shadow:0 0 4px rgba(0,0,0,.12)}
.product .photo{position:absolute;top:12px;left:50%;transform:translateX(-50%);width:64px;height:94px}
.product h4{position:absolute;left:18px;top:114px;font-size:12.5px;font-weight:400;color:#444;letter-spacing:.3px}
.product p{position:absolute;left:18px;top:132px;width:150px;font-size:10px;line-height:16px;color:var(--muted)}

/* news */
.news{left:632px;top:679px;width:244px;height:392px;border:1px solid #e0e0e0;border-radius:3px}
.news header{height:43px;background:linear-gradient(180deg,#2563a3,#0e3b76);border-radius:3px 3px 0 0;color:var(--white);font-size:17px;font-weight:400;padding:12px 19px;letter-spacing:.2px}
.news article{position:absolute;left:19px;width:210px}
.news h4{font-size:13px;font-weight:400;color:var(--navy);margin-bottom:2px}
.news p{font-size:10.3px;line-height:14px;color:#666}

/* footer */
.footer{left:0;top:1103px;width:991px;height:97px;background:linear-gradient(180deg,#1f5a96 0%,#0b2b5c 100%)}
.footer .links{position:absolute;left:82px;top:26px;font-size:11px;font-weight:600;color:var(--white)}
.footer .links span{padding:0 4px}
.footer .links span:first-child{padding-left:0}
.footer .copy{position:absolute;left:82px;top:48px;font-size:10px;color:#bfcde2}
.social{position:absolute;left:815px;top:26px;display:flex;gap:4px}
.social i{display:block;width:21px;height:21px;border-radius:50%;background:var(--white)}
</style>
</head>
<body>
<div class="page">
  <div class="abs logo">Velmint</div>
  <div class="abs slogan">your slaogan goes here</div>
  <div class="abs search">Search here..
    <svg width="15" height="15" viewBox="0 0 15 15"><circle cx="6" cy="6" r="4.5" fill="none" stroke="#999" stroke-width="2"/><line x1="9.5" y1="9.5" x2="13.5" y2="13.5" stroke="#999" stroke-width="2.4" stroke-linecap="round"/></svg>
  </div>
  <nav class="abs nav"><span>Home</span><span>About Us</span><span>What We Do</span><span>Our Projects</span><span>Products</span><span>News</span><span>Contact</span></nav>

  <section class="abs hero">
    <div class="abs map" role="img" aria-label="Faint world map outline"></div>
    <h1 class="abs">World News &amp; Media Services</h1>
    <h2 class="abs">Class aptent taciti sociosqu</h2>
    <p class="abs">Aliquam nec erat at purus cursus interdum. Vestibulum ligula augue, bibendum accumsan, vestibulum ut, commodo</p>
    <div class="abs dots"><i class="on"></i><i></i><i></i><i></i></div>
  </section>

  <h2 class="abs section-title featured-title">Featured Projects</h2>
  <div class="abs project" style="left:19px">
    <div class="photo" role="img" aria-label="Speakers at a podium on a stage" style="background:linear-gradient(90deg,#7a1e14,#b8502a 45%,#3a2a24)"></div>
    <h3>Project Tittle</h3><p>Cum sociis natoque penatibus et magnis dis parturient montes</p>
  </div>
  <div class="abs project" style="left:218px">
    <div class="photo" role="img" aria-label="Crowd at a rally holding a sign" style="background:linear-gradient(135deg,#3f6fa8,#8d9fb4 50%,#b38366)"></div>
    <h3>Project Tittle</h3><p>Cum sociis natoque penatibus et magnis dis parturient montes</p>
  </div>
  <div class="abs project" style="left:418px">
    <div class="photo" role="img" aria-label="Team meeting around a table" style="background:linear-gradient(135deg,#c9ccd1,#2a3d55 50%,#9aa3ae)"></div>
    <h3>Project Tittle</h3><p>Cum sociis natoque penatibus et magnis dis parturient montes</p>
  </div>

  <div class="abs video">
    <div class="photo" role="img" aria-label="Speaker in front of press microphones"></div>
    <svg width="34" height="34" viewBox="0 0 34 34"><circle cx="17" cy="17" r="15" fill="rgba(0,0,0,.35)" stroke="#fff" stroke-width="2.5"/><path d="M14 11 L23 17 L14 23 Z" fill="#fff"/></svg>
    <h3>Watch Our Video</h3>
    <p>Cum sociis natoque penatibus et magnis dis parturient montes, nascetur ridiculus mus</p>
  </div>

  <div class="welcome">
    <h2>Welcome to Our Website Mainpage</h2>
    <p>Aliquam nec erat at purus cursus interdum. Vestibulum ligula augue, bibendum accumsan, vestibulum ut, commodo a, mi. Morbi ornare gravida elit. Integer congue, augue et malesuada iaculis, ipsum dui aliquet felis Etiam eu urna. Sed porta. Suspendisse quam leo molestie sed, luctus quis, feugiat in, pede. Fusce tellus. Sed metus augue, convallis et, vehicula ut, pulvinar eu, ante. Integer orci tellus,</p>
  </div>
  <div class="abs divider"></div>

  <h2 class="abs section-title products-title">Latest Products</h2>
  <svg class="abs arrows" width="30" height="20" viewBox="0 0 30 20"><path d="M9 2 L2 10 L9 18" fill="none" stroke="#999" stroke-width="1.6"/><path d="M21 2 L28 10 L21 18" fill="none" stroke="#999" stroke-width="1.6"/></svg>

  <div class="abs product" style="left:26px">
    <div class="photo" role="img" aria-label="Blue book cover standing upright" style="background:linear-gradient(180deg,#4d6a96,#2d4670)"></div>
    <h4>PROUCT NAME</h4><p>Suspendisse quam leo moles-tie sed luctus quis</p>
  </div>
  <div class="abs product" style="left:223px">
    <div class="photo" role="img" aria-label="Book with red spine lying at an angle" style="width:110px;background:linear-gradient(135deg,#e3e3e3,#b9b9b9 60%,#d8344a)"></div>
    <h4>PROUCT NAME</h4><p>Suspendisse quam leo moles-tie sed luctus quis</p>
  </div>
  <div class="abs product" style="left:417px">
    <div class="photo" role="img" aria-label="Dark photo book lying at an angle" style="width:120px;background:linear-gradient(135deg,#2a2a2a,#6a6a6a 50%,#1c1c1c)"></div>
    <h4>PROUCT NAME</h4><p>Suspendisse quam leo moles-tie sed luctus quis</p>
  </div>

  <aside class="abs news">
    <header>RECENT NEWS</header>
    <article style="top:53px"><h4>Cum sociis natoque penatibus</h4><p>Ut nisi erat, fermentum vel, congue id, euis-mod in, elit. Fusce ultricies, orci ac feugiat suscipit, leo massa</p></article>
    <article style="top:129px"><h4>Proin nulla arcu</h4><p>Morbi diam mauris, viverra in, gravida eu, mattis in, ante. Morbi eget arcu. Morbi porta, libero id ullamcorper</p></article>
    <article style="top:210px"><h4>Aliquam nec erat at</h4><p>Morbi diam mauris, viverra in, gravida eu, mattis in, ante. Morbi eget arcu. Morbi porta, libero id ullamcorper</p></article>
    <article style="top:288px"><h4>Class aptent taciti</h4><p>Morbi diam mauris, viverra in, gravida eu, mattis in, ante. Morbi eget arcu. Morbi porta, libero id ullamcorper</p></article>
  </aside>
</div>

<footer class="abs footer">
  <div class="links"><span>Home</span>|<span>About Us</span>|<span>What We Do</span>|<span>Our Projects</span>|<span>Products</span>|<span>News</span>|<span>Contact</span></div>
  <div class="copy">© 2014 Company Name.&nbsp; All right reserved.</div>
  <div class="social" aria-label="Social links"><i></i><i></i><i></i><i></i></div>
</footer>
</body>
</html>
```